Media/PR business needs a website upgrade

Modernise my website www.vrl.net.au into a simpler and mobile friendly site with the usual plugins, maximum 5 pages, 4 might be enough. My page is already hosted and I have an email address so I just want to work with a designer who is fantastic with WordPress, to refresh and simplify the 6 year-old look.

Target Market(s)

men & women 25-55

Industry/Entity Type

Business

Coding

Coded - Design and coding required

Number of Pages Required

4 page

Font styles to use
Sans Serif

Colors
f37122
ffffff

Requirements
Must have
• Social media plugins, about, client portfolio, contact (can be under about)blog capability
Nice to have
• photos of jobs I've done
Should not have
• e-commerce, can lose all the client logos

```html
<!DOCTYPE html>
<html lang="en">
<head>
<meta charset="utf-8">
<title>Vantage Reef Liaison</title>
<link rel="stylesheet" href="https://fonts.googleapis.com/css2?family=Bebas+Neue&family=Raleway:ital,wght@0,400;0,500;0,600;1,400&family=Roboto:wght@400;500;700&display=swap">
<style>
:root{
  --orange:#f37122;
  --orange-deep:#c0701e;
  --ink:#222222;
  --text:#555555;
  --muted:#777777;
  --dark:#2b1d1a;
  --white:#ffffff;
  --line:#e3e3e3;
  --brand-gold:#a87a44;
}
*{box-sizing:border-box;margin:0;padding:0}
html,body{width:1200px;height:2582px;overflow:hidden;background:var(--white)}
body{position:relative;font-family:"Raleway",sans-serif;color:var(--text)}
.abs{position:absolute}

/* header */
.site-header{position:absolute;left:0;top:0;width:1200px;height:107px;background:var(--orange)}
.logo-panel{position:absolute;left:0;top:0}
.brand{position:absolute;left:86px;top:12px;display:flex;align-items:center;gap:12px}
.brand-dot{width:82px;height:82px;border-radius:50%;background:var(--orange)}
.brand-name{font-family:"Roboto",sans-serif;font-weight:700;font-size:21px;line-height:23px;color:var(--ink)}
.topbar{position:absolute;left:685px;top:0;width:515px;height:41px;background:var(--dark);border-bottom-left-radius:22px;display:flex;align-items:center;padding-left:40px;gap:26px;font-family:"Roboto",sans-serif;font-size:15px;color:var(--white)}
.topbar .item{display:flex;align-items:center;gap:7px}
.socials{display:flex;gap:12px;margin-left:6px}
.socials span{width:12px;height:12px;border-radius:50%;background:var(--orange)}
.main-nav{position:absolute;left:394px;top:62px;display:flex;gap:34px;font-family:"Roboto",sans-serif;font-size:16px;color:var(--white)}

/* hero */
.hero{position:absolute;left:0;top:107px;width:1200px;height:568px;background:linear-gradient(180deg,#7a7f80 0%,#9a9890 22%,#6f655a 40%,#5c4f43 65%,#4a3e33 100%)}
.hero-title{position:absolute;left:83px;top:300px;font-family:"Roboto",sans-serif;font-weight:700;font-size:50px;line-height:56px;color:var(--white);text-transform:uppercase}
.hero-sub{position:absolute;left:83px;top:430px;font-family:"Raleway",sans-serif;font-size:27px;color:var(--white)}

/* welcome */
.welcome{position:absolute;left:86px;top:640px;width:1028px;height:245px;background:var(--white);box-shadow:0 18px 22px -14px rgba(0,0,0,.35);border:1px solid #eee;padding:24px 38px}
.welcome .kicker{font-family:"Raleway",sans-serif;font-size:23px;color:var(--orange)}
.welcome h2{font-family:"Roboto",sans-serif;font-weight:700;font-size:29px;color:var(--ink);margin-top:0}
.welcome p{font-size:14.5px;line-height:23px;color:var(--muted);margin-top:14px}

/* section titles */
.section-title{position:absolute;left:0;width:1200px;text-align:center;font-family:"Bebas Neue",sans-serif;font-size:50px;color:var(--ink);letter-spacing:.5px}
.divider{position:absolute;left:512px;width:176px;height:2px;background:var(--orange)}
.divider::after{content:"";position:absolute;left:66px;top:-3px;width:44px;height:8px;border-radius:4px;background:var(--orange)}

/* services */
.service-card{position:absolute;top:1064px;width:318px;height:348px;background:var(--white);border:1px solid var(--line);box-shadow:0 2px 4px rgba(0,0,0,.06);overflow:hidden}
.service-card .photo{height:198px}
.service-card h3{margin:24px 0 0 18px;padding-left:12px;border-left:4px solid var(--orange);font-family:"Roboto",sans-serif;font-weight:700;font-size:14px;line-height:16px;color:var(--ink);text-transform:uppercase}
.service-card p{margin:14px 18px 0 26px;font-size:12.5px;line-height:22px;color:var(--muted)}
.slider-arrow{position:absolute;top:1178px;width:46px;height:46px;background:rgba(30,30,30,.85);display:flex;align-items:center;justify-content:center}

/* projects */
.projects-feature{position:absolute;left:0;top:1482px;width:448px;height:383px;background:linear-gradient(180deg,#2a2a30,#3c3230 60%,#2c2420)}
.projects-label{position:absolute;left:86px;top:1650px;font-family:"Bebas Neue",sans-serif;font-size:44px;color:var(--white)}
.tile{position:absolute;width:201px;height:187px}
.tile-info{background:#3b3f4a;padding:13px}
.tile-info div{border:1px solid rgba(255,255,255,.6);height:100%;display:flex;align-items:center;justify-content:center;text-align:center;font-family:"Raleway",sans-serif;font-size:14px;line-height:23px;color:var(--white)}

/* testimonials */
.quote-card{position:absolute;top:2040px;width:496px;height:224px;border:1px solid #f4c89f;background:var(--white);padding:30px 16px 0 16px}
.quote-mark{position:absolute;top:-16px;left:32px;background:var(--white);padding:0 6px;font-family:"Roboto",sans-serif;font-weight:700;font-size:40px;line-height:32px;color:var(--orange)}
.quote-card p{font-style:italic;font-size:12.5px;line-height:23.5px;color:var(--text)}
.quote-card .author{margin-top:12px;font-style:italic;font-size:12.5px;line-height:23px;color:var(--orange)}
.chev{position:absolute;top:2125px}

/* footer */
.site-footer{position:absolute;left:0;top:2336px;width:1200px;height:246px;background:var(--dark)}
.footer-heading{font-family:"Roboto",sans-serif;font-weight:700;font-size:20px;color:var(--white)}
.footer-about{position:absolute;left:86px;top:2360px;width:450px}
.footer-about p{font-size:12.5px;line-height:22px;color:var(--white);margin-top:4px}
.footer-about p + p{margin-top:16px}
.footer-socials{display:flex;gap:18px;margin-top:12px}
.footer-socials span{width:12px;height:12px;border-radius:50%;background:var(--white)}
.newsletter{position:absolute;left:599px;top:2360px;width:280px}
.email-field{margin-top:20px;width:270px;height:44px;border:1px solid rgba(255,255,255,.45);padding:0 14px;display:flex;align-items:center;font-size:13px;color:#bbb}
.subscribe{margin-top:18px;width:153px;height:42px;background:var(--brand-gold);color:var(--white);display:flex;align-items:center;justify-content:center;font-family:"Roboto",sans-serif;font-size:20px}
.contact{position:absolute;left:896px;top:2360px;width:280px;color:var(--white)}
.contact .row{display:flex;align-items:center;gap:7px;margin-top:10px;font-family:"Roboto",sans-serif;font-size:16px}
.contact .small{font-size:12.5px}
</style>
</head>
<body>

<header class="site-header">
  <svg class="logo-panel" width="380" height="107" aria-hidden="true"><polygon points="0,0 370,0 354,107 0,107" fill="#ffffff"/></svg>
  <div class="brand">
    <span class="brand-dot"></span>
    <span class="brand-name">Vantage<br>Reef<br>Liaison</span>
  </div>
  <div class="topbar">
    <span class="item">
      <svg width="13" height="13" viewBox="0 0 24 24"><path fill="#f37122" d="M6.6 10.8a15 15 0 0 0 6.6 6.6l2.2-2.2c.3-.3.7-.4 1-.2 1.1.4 2.3.6 3.6.6.6 0 1 .4 1 1V20c0 .6-.4 1-1 1A17 17 0 0 1 3 4c0-.6.4-1 1-1h3.5c.6 0 1 .4 1 1 0 1.3.2 2.5.6 3.6.1.3 0 .7-.2 1z"/></svg>
      0400 555 019
    </span>
    <span class="item">
      <svg width="15" height="12" viewBox="0 0 24 18"><rect x="0" y="0" width="24" height="18" rx="2" fill="#f37122"/><path d="M1 2l11 8 11-8" stroke="#2b1d1a" stroke-width="2" fill="none"/></svg>
      nadia@vrl.net.au
    </span>
    <span class="socials"><span></span><span></span><span></span></span>
  </div>
  <nav class="main-nav">
    <span>Home</span><span>Services</span><span>About</span><span>Client</span><span>Portfolio</span><span>Testimonials</span><span>Blog</span><span>Contact</span>
  </nav>
</header>

<section class="hero" role="img" aria-label="Photo of a sandy beach at the water's edge with gulls and a pelican in flight"></section>
<h1 class="hero-title">Vantage Reef<br>Liaison</h1>
<p class="hero-sub">is an established specialist public relations and event management business.</p>

<section class="welcome">
  <div class="kicker">Welcome to</div>
  <h2>Vantage Reef Liaison</h2>
  <p>With a communications degree and 20 plus years experience working in public relations, publicity, media and project management, VRL founder Nadia Pemberton offers a complete contract based option for your next major sporting, social, cultural or community event.</p>
  <p>Contact Nadia at VRL for strategic advice on sponsorship spend and how to leverage your investment, and to tap into her extensive media and professional network.</p>
</section>

<h2 class="section-title" style="top:945px">Our Services</h2>
<div class="divider" style="top:1012px"></div>

<article class="service-card" style="left:-270px">
  <div class="photo" role="img" aria-label="Photo of event staff at a venue" style="background:linear-gradient(160deg,#c9c2a8,#8c8a76)"></div>
  <h3>Events</h3>
  <p>Event planning and on-site management for every occasion.</p>
</article>
<article class="service-card" style="left:86px">
  <div class="photo" role="img" aria-label="Photo of racing yachts with white sails on a bay" style="background:linear-gradient(180deg,#c7d6e2,#a9bccb 55%,#6f8ea6)"></div>
  <h3>Sports Media</h3>
  <p>VRL founder Nadia Pemberton has worked closely with Australian and international sports media since 1996.</p>
</article>
<article class="service-card" style="left:441px">
  <div class="photo" role="img" aria-label="Photo of a sailing dinghy crew hiking out in racing" style="background:linear-gradient(180deg,#b8bec4,#8e979e 60%,#5e666c)"></div>
  <h3>Publicity</h3>
  <p>Generating media publicity for both the event and its sponsor is one of Nadia's key strengths and drivers.</p>
</article>
<article class="service-card" style="left:797px">
  <div class="photo" role="img" aria-label="Photo of a woman aboard a speeding motor boat on open water" style="background:linear-gradient(180deg,#b9c6cf,#7b8f9c 50%,#4f6373)"></div>
  <h3>Sponsorship Leverage</h3>
  <p>Nadia has worked with many sponsors including premium brand clients Meridian Watches and Australia, Harbour Motors and Northline Cars.</p>
</article>
<article class="service-card" style="left:1150px">
  <div class="photo" role="img" aria-label="Photo of a waterfront promotion" style="background:linear-gradient(180deg,#c3ccd3,#8a98a3)"></div>
  <h3>Promotion</h3>
  <p>Lending your event a clear voice.</p>
</article>
<div class="slider-arrow" style="left:0"><svg width="12" height="18"><path d="M9 2L3 9l6 7" stroke="#fff" stroke-width="2.5" fill="none"/></svg></div>
<div class="slider-arrow" style="left:1154px"><svg width="12" height="18"><path d="M3 2l6 7-6 7" stroke="#fff" stroke-width="2.5" fill="none"/></svg></div>

<section>
  <div class="projects-feature" role="img" aria-label="Photo of a group of event guests posing together at an evening function"></div>
  <h2 class="projects-label">Projects/Events:</h2>
  <div class="tile tile-info" style="left:499px;top:1482px"><div>PR/ Communications<br>Consultant<br>September 2016<br>Current<br>Coral Key Resorts Limited</div></div>
  <div class="tile" style="left:706px;top:1482px;background:linear-gradient(180deg,#8fb3d3,#6c8aa8 55%,#b9593a)" role="img" aria-label="Photo of people on a rescue boat in a harbour"></div>
  <div class="tile" style="left:913px;top:1482px;background:linear-gradient(180deg,#d7dde4,#6f6a68)" role="img" aria-label="Photo of a group at a sponsor media wall"></div>
  <div class="tile" style="left:499px;top:1675px;background:linear-gradient(180deg,#c7ccd1,#8f9489 60%,#6e7c82)" role="img" aria-label="Photo of two women on a boat at a regatta"></div>
  <div class="tile" style="left:706px;top:1675px;background:linear-gradient(180deg,#9fc7e7,#3d8ec9 55%,#2a6ea8)" role="img" aria-label="Photo of yachts racing on blue water"></div>
  <div class="tile" style="left:913px;top:1675px;background:linear-gradient(180deg,#c7bdb5,#8b6b5e 60%,#5e4a43)" role="img" aria-label="Photo of guests holding drinks at a reception"></div>
</section>

<h2 class="section-title" style="top:1923px">Testimonials</h2>
<div class="divider" style="top:1990px"></div>

<article class="quote-card" style="left:86px">
  <span class="quote-mark">&ldquo;</span>
  <p>Coral Key has contracted Nadia as the event journalist then media manager and part of the PR effort for Coral Key Race Week since 2005. Through her impressive competitor and media network she continues to deliver great results in terms of the coverage achieved and the smooth running of the media operation...</p>
  <div class="author">Martin Ashby<br>Coral Key CEO, 2 March 2014</div>
</article>
<article class="quote-card" style="left:618px">
  <span class="quote-mark">&ldquo;</span>
  <p>Coral Key has contracted Nadia as the event journalist then media manager and part of the PR effort for Coral Key Race Week since 2005. Through her impressive competitor and media network she continues to deliver great results in terms of the coverage achieved and the smooth running of the media operation...</p>
  <div class="author">Martin Ashby<br>Coral Key CEO, 2 March 2014</div>
</article>
<svg class="chev" style="left:46px" width="16" height="66"><path d="M14 2L3 33l11 31" stroke="#444" stroke-width="1.5" fill="none"/></svg>
<svg class="chev" style="left:1138px" width="16" height="66"><path d="M2 2l11 31-11 31" stroke="#444" stroke-width="1.5" fill="none"/></svg>

<footer class="site-footer">
  <svg class="abs" style="left:0;top:0" width="580" height="246" aria-hidden="true"><polygon points="0,0 577,0 525,246 0,246" fill="#c0701e"/></svg>
</footer>
<div class="footer-about">
  <div class="footer-heading">ABOUT US</div>
  <p>Nadia grew up on Gull Island in Eastwater on the city's northern beaches, the breeding ground for many Australian sailing greats including the Harlows, Fennicks and the Drakes.</p>
  <p>As a 'tinny terror' she attended Bay Vale Public School then Eastwater High School with some ...</p>
  <div class="footer-socials"><span></span><span></span><span></span></div>
</div>
<div class="newsletter">
  <div class="footer-heading">NEWSLETTER</div>
  <div class="email-field">Your Email</div>
  <div class="subscribe">SUBSCRIBE</div>
</div>
<div class="contact">
  <div class="footer-heading">ABOUT US</div>
  <div class="row"><svg width="14" height="14" viewBox="0 0 24 24"><path fill="#f37122" d="M6.6 10.8a15 15 0 0 0 6.6 6.6l2.2-2.2c.3-.3.7-.4 1-.2 1.1.4 2.3.6 3.6.6.6 0 1 .4 1 1V20c0 .6-.4 1-1 1A17 17 0 0 1 3 4c0-.6.4-1 1-1h3.5c.6 0 1 .4 1 1 0 1.3.2 2.5.6 3.6.1.3 0 .7-.2 1z"/></svg>+61 400 555 019</div>
  <div class="row small"><svg width="10" height="14" viewBox="0 0 20 28"><path fill="#f37122" d="M10 0a10 10 0 0 0-10 10c0 7 10 18 10 18s10-11 10-18A10 10 0 0 0 10 0zm0 14a4 4 0 1 1 0-8 4 4 0 0 1 0 8z"/></svg>PO BOX 2210,<br></div>
  <div class="small" style="margin-top:4px">BAY VALE NSW 2999 AUSTRALIA</div>
  <div class="row"><svg width="15" height="12" viewBox="0 0 24 18"><rect width="24" height="18" rx="2" fill="#f37122"/><path d="M1 2l11 8 11-8" stroke="#2b1d1a" stroke-width="2" fill="none"/></svg>NADIA@VRL.NET.AU</div>
  <div class="row" style="margin-top:16px;font-size:15px">ABN: 12 345 678 901</div>
</div>

</body>
</html>
```